Corwell Facilities Services Business Card.

We need a card for Corwell Facilities Services with a new look. We also have service and supply partners that we would like to have on the card. Lumacoat is a surface application company, Corwell Facilities is a facilities services business, Tavish Supply Co is a Facilities supply business, Pelvra is a product that we use that powers our business.

```html
<!DOCTYPE html>
<html lang="en">
<head>
<meta charset="utf-8">
<title>Corwell Facilities Services – Business Card</title>
<link rel="stylesheet" href="https://fonts.googleapis.com/css2?family=Open+Sans:wght@400;600;700;800&family=Lato:wght@400;700&display=swap">
<style>
  :root {
    --backdrop: #3b3430;
    --card: #2f3032;
    --card-band: #28292b;
    --rule: #4a4b4e;
    --brand-blue: #1e7fd0;
    --brand-green: #3cb54a;
    --text-light: #f1f1f1;
    --text-muted: #d6d6d6;
  }
  * { box-sizing: border-box; margin: 0; padding: 0; }
  html, body { width: 1200px; height: 795px; overflow: hidden; }
  body {
    background: var(--backdrop);
    font-family: "Lato", "Open Sans", sans-serif;
    position: relative;
  }
  .card {
    position: absolute;
    top: 249px;
    width: 520px;
    height: 297px;
    background: var(--card);
    border-radius: 4px;
    overflow: hidden;
    box-shadow: 0 14px 30px rgba(0,0,0,0.45);
  }
  .card--front { left: 50px; }
  .card--back { left: 630px; }

  /* Front */
  .front-brand {
    position: absolute;
    left: 0; right: 0; top: 0; height: 168px;
    display: flex; flex-direction: column; align-items: center; justify-content: center;
  }
  .brand-name {
    font-family: "Open Sans", sans-serif;
    font-weight: 800;
    color: var(--brand-blue);
    line-height: 1;
    letter-spacing: -1px;
  }
  .brand-sub {
    font-family: "Open Sans", sans-serif;
    font-weight: 600;
    color: var(--brand-blue);
  }
  .front-brand .brand-name { font-size: 62px; }
  .front-brand .brand-sub { font-size: 22px; margin-top: 4px; }
  .partner-band {
    position: absolute;
    left: 0; right: 0; bottom: 0; height: 129px;
    background: var(--card-band);
    border-top: 1px solid var(--rule);
    display: flex; align-items: center; justify-content: space-around;
    padding: 0 20px;
  }
  .partner {
    display: flex; flex-direction: column; align-items: center;
    font-family: "Open Sans", sans-serif;
    font-weight: 700;
    color: var(--brand-blue);
    font-size: 20px;
  }
  .partner--tavish { color: #5a86c8; }
  .partner--lumacoat { color: #3fa3d8; }
  .partner--pelvra { color: var(--text-light); font-size: 26px; letter-spacing: 2px; }
  .partner-note {
    font-family: "Lato", sans-serif;
    font-weight: 400;
    font-size: 12px;
    color: var(--text-light);
    letter-spacing: 0;
    margin-bottom: 2px;
  }

  /* Back */
  .back-brand {
    position: absolute;
    left: 120px; top: 36px;
  }
  .back-brand .brand-name { font-size: 40px; }
  .back-brand .brand-sub { font-size: 15px; margin-top: 2px; }
  .address {
    position: absolute;
    left: 104px; top: 128px;
    color: var(--text-light);
    font-size: 14px;
    line-height: 1.45;
  }
  .contact-list {
    position: absolute;
    left: 60px; top: 196px;
    list-style: none;
    color: var(--text-light);
    font-size: 14px;
    line-height: 1.5;
  }
  .contact-list li { display: flex; align-items: center; gap: 6px; }
  .contact-list svg { width: 11px; height: 11px; fill: var(--brand-blue); flex: none; }
  .person {
    position: absolute;
    right: 70px; bottom: 48px;
    text-align: right;
  }
  .person-name {
    font-family: "Open Sans", sans-serif;
    font-weight: 600;
    font-size: 19px;
    color: var(--brand-blue);
    letter-spacing: 0.5px;
  }
  .person-title {
    font-size: 15px;
    color: var(--text-light);
    margin-top: 2px;
  }
</style>
</head>
<body>
  <section class="card card--front" aria-label="Card front">
    <div class="front-brand">
      <div class="brand-name">Corwell</div>
      <div class="brand-sub">Facilities Services</div>
    </div>
    <div class="partner-band">
      <div class="partner partner--tavish">Tavish Supply Co</div>
      <div class="partner partner--lumacoat">Lumacoat</div>
      <div class="partner partner--pelvra">
        <span class="partner-note">Powered by</span>
        Pelvra
      </div>
    </div>
  </section>

  <section class="card card--back" aria-label="Card back">
    <div class="back-brand">
      <div class="brand-name">Corwell</div>
      <div class="brand-sub">Facilities Services</div>
    </div>
    <p class="address">Street Avenue, Suite 100<br>State, Zip Code, Country</p>
    <ul class="contact-list">
      <li>
        <svg viewBox="0 0 24 24" aria-hidden="true"><path d="M6.6 10.8a15.1 15.1 0 0 0 6.6 6.6l2.2-2.2c.3-.3.7-.4 1-.2 1.1.4 2.3.6 3.6.6.6 0 1 .4 1 1V20c0 .6-.4 1-1 1A17 17 0 0 1 3 4c0-.6.4-1 1-1h3.5c.6 0 1 .4 1 1 0 1.3.2 2.5.6 3.6.1.3 0 .7-.2 1z"/></svg>
        555-014-2290
      </li>
      <li>
        <svg viewBox="0 0 24 24" aria-hidden="true"><path d="M2 5h20v14H2z M2 5l10 8 10-8" /></svg>
        info@corwellfs.example
      </li>
      <li>
        <svg viewBox="0 0 24 24" aria-hidden="true"><circle cx="12" cy="12" r="10"/></svg>
        www.corwellfs.example
      </li>
    </ul>
    <div class="person">
      <div class="person-name">DANA WHITLOCK</div>
      <div class="person-title">Founder &amp; CEO</div>
    </div>
  </section>
</body>
</html>
```